Corporate Stationary for Beverage Alcohol Company
Brook Harbor Global Ltd. Co.
Corporate Stationary for Beverage Alcohol Company - Beverages
Creative Brief
Corporate
Dean Walter Prosser
President
512 Fenwood Drive Lexford, KY 40311
dean.prosser@brook-harbor.com
www.brook-harbor.com
The stationary shall be cutting edge and will utilize the logo art work. I would like an abstract border included on the side(s) of the letterhead, envelope and the business card.
Company Name Logo Abstract border

```html
<!DOCTYPE html>
<html lang="en">
<head>
<meta charset="utf-8">
<title>Brook Harbor Global – Business Card</title>
<link href="https://fonts.googleapis.com/css2?family=Cinzel:wght@500;600&family=Libre+Baskerville:wght@400&display=swap" rel="stylesheet">
<style>
  :root {
    --backdrop: #d9d9d9;
    --gold-light: #f2c25a;
    --gold-mid: #e0a532;
    --gold-deep: #b97e1c;
    --ink: #3a3a3a;
    --ink-dark: #2e2a24;
    --ink-soft: #666;
    --paper: #ffffff;
    --rule: #d8d8d8;
  }
  * { box-sizing: border-box; margin: 0; padding: 0; }
  html, body { width: 1200px; height: 871px; overflow: hidden; }
  body {
    background: var(--backdrop);
    font-family: "Libre Baskerville", Georgia, serif;
    color: var(--ink);
    display: flex;
    flex-direction: column;
    align-items: center;
    justify-content: center;
    gap: 30px;
  }
  .card {
    width: 680px;
    height: 388px;
    position: relative;
    overflow: hidden;
    box-shadow: 0 4px 14px rgba(0,0,0,.18);
  }

  /* Back side */
  .card-back { display: flex; align-items: center; justify-content: center; }
  .card-back .pattern-field {
    position: absolute; inset: 0;
    background: radial-gradient(ellipse at 45% 40%, var(--gold-light) 0%, var(--gold-mid) 55%, var(--gold-deep) 100%);
  }
  .brand-lockup {
    position: relative;
    display: flex; flex-direction: column; align-items: center; gap: 14px;
  }
  .brand-mark {
    width: 46px; height: 46px; border-radius: 50%;
    background: var(--paper);
  }
  .brand-name {
    font-family: "Cinzel", serif;
    font-weight: 600;
    font-size: 30px;
    letter-spacing: 1px;
    color: var(--ink-dark);
    white-space: nowrap;
  }
  .brand-tagline {
    font-family: "Cinzel", serif;
    font-size: 10px;
    letter-spacing: 3px;
    color: var(--ink-dark);
  }

  /* Front side */
  .card-front { background: var(--paper); }
  .front-logo {
    position: absolute; left: 34px; top: 96px; width: 300px;
    display: flex; flex-direction: column; align-items: center; gap: 10px;
  }
  .front-logo .brand-mark { background: var(--gold-mid); width: 40px; height: 40px; }
  .front-logo .brand-name { font-size: 20px; }
  .front-logo .brand-tagline { font-size: 7px; color: var(--gold-deep); }
  .divider {
    position: absolute; left: 366px; top: 34px; width: 1px; height: 252px;
    background: var(--rule);
  }
  .contact { position: absolute; left: 394px; top: 42px; }
  .person-name {
    font-family: "Cinzel", serif; font-weight: 500;
    font-size: 17px; color: var(--ink);
  }
  .person-title {
    font-family: "Cinzel", serif; font-size: 12px;
    color: var(--gold-mid); margin-top: 4px;
  }
  .address { font-size: 12px; line-height: 19px; color: var(--ink-soft); margin-top: 30px; }
  .contact-lines { margin-top: 22px; font-size: 12px; line-height: 22px; color: var(--ink-soft); }
  .contact-line { display: flex; align-items: center; gap: 8px; white-space: nowrap; }
  .contact-line svg { width: 11px; height: 11px; fill: var(--gold-mid); flex: none; }
  .footer-rule {
    position: absolute; left: 0; right: 0; bottom: 52px; height: 3px;
    background: var(--gold-mid);
  }
  .footer-band {
    position: absolute; left: 0; right: 0; bottom: 0; height: 44px;
    background: linear-gradient(90deg, var(--gold-deep), var(--gold-light) 50%, var(--gold-deep));
    display: flex; align-items: center; justify-content: center;
  }
  .website { font-size: 12px; letter-spacing: 3px; color: var(--paper); }
</style>
</head>
<body>
  <section class="card card-back">
    <div class="pattern-field" role="img" aria-label="Gold background with a fine repeating ornamental pattern"></div>
    <div class="brand-lockup">
      <span class="brand-mark"></span>
      <span class="brand-name">BROOK HARBOR GLOBAL</span>
      <span class="brand-tagline">CRAFT AND HERITAGE</span>
    </div>
  </section>

  <section class="card card-front">
    <div class="front-logo">
      <span class="brand-mark"></span>
      <span class="brand-name">BROOK HARBOR GLOBAL</span>
      <span class="brand-tagline">CRAFT AND HERITAGE</span>
    </div>
    <div class="divider"></div>
    <div class="contact">
      <p class="person-name">Dean Walter Prosser</p>
      <p class="person-title">President</p>
      <p class="address">512 Fenwood Drive<br>Lexford, KY 40311</p>
      <div class="contact-lines">
        <p class="contact-line">
          <svg viewBox="0 0 24 24" aria-hidden="true"><path d="M6.6 10.8a15 15 0 0 0 6.6 6.6l2.2-2.2a1 1 0 0 1 1-.25 11.4 11.4 0 0 0 3.6.57 1 1 0 0 1 1 1V20a1 1 0 0 1-1 1A17 17 0 0 1 3 4a1 1 0 0 1 1-1h3.5a1 1 0 0 1 1 1c0 1.25.2 2.45.57 3.57a1 1 0 0 1-.25 1z"/></svg>
          (859)-555-0142
        </p>
        <p class="contact-line">
          <svg viewBox="0 0 24 24" aria-hidden="true"><path d="M2 5h20v14H2z M4 7v.4l8 5 8-5V7z" fill-rule="evenodd"/></svg>
          dean.prosser@brook-harbor.com
        </p>
      </div>
    </div>
    <div class="footer-rule"></div>
    <div class="footer-band"><span class="website">www.brook-harbor.com</span></div>
  </section>
</body>
</html>
```